New Therapist Looking for Unique Fun Exciting Brochure for Private Practice

I need a basic brochure displaying my services for my new therapy/counseling business. My company is Stone and Brook PLLC and I would like something that looks earthy with green colors similar to my logo. I want just my logo and my name on the front. I would like a few pictures throughout that include trees and I have added them as uploads. I want it simple, playful and earthy with just my services, business details, my prices, qualifications, mission statement and maybe a quote. I am very authentic and want it to really represent me.

I offer mental health and substance abuse counseling for ages 14 and up. I also do body based work like yoga, breath and medication in my practice.

Will provide text content to winner - please use place holders for now.

Target Market(s)

Behavioral Health hospitals, psychiatrists, doctors, medical professionals, other therapists, substance use treatment centers, holistic practitioners

Industry/Entity Type

Counseling

Font styles to use
Serif

Colors
61bae0
85cae6
9bcb3c
abd037
cadf82
f68e4e
00a990
fbf289

Requirements
Must have
• An authentic feel, earthy and inviting - must include at least one tree picture that I included and my logo, must include one of my profile pictures
Nice to have
• Open - maybe greens and earthy tones similar to my logo
Should not have
• open

```html
<!DOCTYPE html>
<html lang="en">
<head>
<meta charset="utf-8">
<title>Stone and Brook PLLC — Brochure</title>
<link rel="stylesheet" href="https://fonts.googleapis.com/css2?family=Allura&family=Amatic+SC:wght@700&family=Roboto+Condensed:ital,wght@0,300;0,400;0,700;1,700&family=Roboto:wght@300;400&display=swap">
<style>
  :root {
    --leaf: #7dc242;
    --teal: #1aae88;
    --deep-teal: #119a80;
    --clay: #c58443;
    --amber: #f7941d;
    --ink: #1d1d1d;
    --grey: #555;
    --paper: #ffffff;
  }
  * { margin: 0; padding: 0; box-sizing: border-box; }
  html, body { width: 1200px; height: 777px; overflow: hidden; background: var(--paper); }
  .brochure { position: relative; width: 1200px; height: 777px; overflow: hidden; background: var(--paper); font-family: "Roboto Condensed", sans-serif; color: var(--ink); }
  .abs { position: absolute; }

  /* left panel */
  .about-title { left: 42px; top: 50px; font-family: "Roboto", sans-serif; font-weight: 300; font-size: 36px; color: var(--leaf); }
  .intro { left: 42px; width: 215px; font-size: 15.5px; line-height: 19px; font-weight: 400; }
  .intro-1 { top: 103px; }
  .intro-2 { top: 162px; }
  .intro-3 { top: 237px; }
  .highlight { font-style: italic; font-weight: 700; font-size: 25px; line-height: 31px; color: var(--clay); }
  .story { left: 42px; top: 343px; width: 207px; font-size: 11.6px; line-height: 15.2px; color: var(--grey); text-align: justify; font-weight: 400; }
  .mission-title { left: 42px; top: 542px; font-size: 12px; font-weight: 700; color: #444; }
  .mission { left: 42px; top: 557px; width: 207px; font-size: 11.6px; line-height: 15.2px; color: var(--grey); text-align: justify; }

  /* center column */
  .clay-column { left: 300px; top: 0; width: 300px; height: 777px; background: var(--clay); }
  .photo-frame { left: 260px; top: 28px; width: 300px; height: 391px; background: var(--paper); }
  .portrait { left: 260px; top: 46px; width: 285px; height: 355px; }
  .script { font-family: "Allura", cursive; color: var(--paper); }
  .portrait-name { left: 280px; top: 345px; font-size: 40px; }
  .iam { left: 320px; top: 435px; width: 165px; text-align: center; font-family: "Amatic SC", sans-serif; font-weight: 700; color: var(--paper); }
  .iam-head { font-size: 34px; line-height: 34px; }
  .iam-list { font-size: 19px; line-height: 19.2px; }
  .role { left: 490px; top: 518px; width: 102px; text-align: center; font-family: "Amatic SC", sans-serif; font-weight: 700; color: var(--paper); font-size: 25px; line-height: 21px; }
  .role-icon { left: 527px; top: 568px; }

  /* contact band */
  .band-left { left: 0; top: 624px; width: 300px; height: 116px; background: var(--leaf); }
  .band-mid { left: 300px; top: 624px; width: 300px; height: 116px; background: var(--teal); }
  .name-line { left: 42px; top: 640px; font-size: 21px; color: var(--ink); }
  .creds { left: 42px; top: 664px; font-size: 12.5px; }
  .call { left: 40px; top: 683px; font-size: 23.5px; font-weight: 700; }
  .web { left: 42px; top: 713px; font-family: "Roboto", sans-serif; font-size: 16px; letter-spacing: 3.3px; }
  .address { left: 325px; top: 643px; font-size: 13px; line-height: 16.5px; color: var(--paper); }

  /* cover panel */
  .scene { left: 600px; top: 0; width: 600px; height: 777px; }
  .brand { left: 740px; top: 128px; width: 330px; display: flex; align-items: center; gap: 12px; }
  .brand-dot { width: 30px; height: 30px; border-radius: 50%; background: var(--amber); flex: none; }
  .brand-name { font-family: "Roboto Condensed", sans-serif; font-weight: 400; font-size: 42px; color: var(--deep-teal); white-space: nowrap; }
  .tagline { left: 700px; top: 276px; width: 300px; text-align: right; font-size: 25px; line-height: 34.5px; color: var(--deep-teal); }
  .tagline b { color: var(--amber); font-weight: 700; }
  .cover-name { left: 778px; top: 425px; font-size: 46px; color: var(--ink); }
  .cover-quote { left: 600px; top: 668px; width: 600px; text-align: center; font-size: 24.5px; font-weight: 700; color: #b8641f; letter-spacing: 0.3px; text-shadow: 0 0 6px #fff, 0 0 12px #fff, 0 0 18px #fff; }
</style>
</head>
<body>
<main class="brochure">

  <!-- left panel -->
  <h2 class="abs about-title">About Me</h2>
  <p class="abs intro intro-1">I am very authentic and want it to really represent me.</p>
  <p class="abs intro intro-2">I offer mental health and substance abuse counseling for ages 14 and up.</p>
  <p class="abs intro intro-3">I also do body based work like <span class="highlight">yoga, breath and medication</span> in my practice.</p>
  <p class="abs story">I enjoy working with clients who want to improve the quality of their relationships. As part of supporting clients in addressing relationship issues, my work can involve working with clients on individual issues such as reducing depression and anxiety. I assist clients in exploring and processing feelings that contribute to depression and anxiety with the goal of promoting individual well-being which, in turn, contributes to improvement in relationships.</p>
  <h3 class="abs mission-title">MISSION STATEMENT</h3>
  <p class="abs mission">approach that involves supporting clients in understanding how past life experiences and current life issues are impacting their lives.</p>

  <!-- center column -->
  <div class="abs clay-column"></div>
  <div class="abs photo-frame"></div>
  <svg class="abs portrait" width="285" height="355" role="img" aria-label="Portrait photo of the therapist seated in a grey armchair">
    <defs>
      <linearGradient id="portraitTone" x1="0" y1="0" x2="1" y2="1">
        <stop offset="0" stop-color="#2a2522"/>
        <stop offset="0.5" stop-color="#4a3f36"/>
        <stop offset="1" stop-color="#1c1a19"/>
      </linearGradient>
    </defs>
    <rect width="285" height="355" fill="url(#portraitTone)"/>
  </svg>
  <div class="abs script portrait-name">Your Name here</div>

  <div class="abs iam">
    <div class="iam-head">I AM A</div>
    <div class="iam-list">PAIN REMOVING<br>HEALTH IMPROVING<br>BACK REPAIRING<br>ALWAYS CARING<br>MUSCLE KNEADING<br>STRESS RELIEVING<br>MIRACLE WORKING</div>
  </div>
  <div class="abs role">MASSAGE<br>THERAPIST</div>
  <svg class="abs role-icon" width="28" height="28" aria-hidden="true">
    <circle cx="14" cy="14" r="14" fill="#fff"/>
    <path d="M10 16 V9.5 a1.2 1.2 0 0 1 2.4 0 V14 V8 a1.2 1.2 0 0 1 2.4 0 V14 V9 a1.2 1.2 0 0 1 2.4 0 V15 l1.4-1.6 a1.2 1.2 0 0 1 1.8 1.5 L17 20.5 Q15.5 22 13 22 Q10 22 10 19 Z" fill="var(--clay)"/>
  </svg>

  <!-- contact band -->
  <div class="abs band-left"></div>
  <div class="abs band-mid"></div>
  <div class="abs name-line">Your Name MFT, LPCC</div>
  <div class="abs creds">Marriage &amp; Family Therapist, MS, MFT, LPCC</div>
  <div class="abs call">Call Now (555) 218-4093</div>
  <div class="abs web">www.yourwebsite.com</div>
  <address class="abs address" style="font-style:normal">Quiet Harbor Wellness, LLC<br>418 Linden Hollow Rd<br>Suite 12<br>Millbrook, Virginia 23190<br>(555) 218-4093</address>

  <!-- cover panel -->
  <svg class="abs scene" width="600" height="777" role="img" aria-label="Photo of a lone tree in a red rock desert canyon under a cloudy sky">
    <defs>
      <linearGradient id="sceneTone" x1="0" y1="0" x2="0" y2="1">
        <stop offset="0" stop-color="#ffffff"/>
        <stop offset="0.33" stop-color="#ffffff"/>
        <stop offset="0.5" stop-color="#e3eef6"/>
        <stop offset="0.66" stop-color="#c9dcec"/>
        <stop offset="0.78" stop-color="#c98a5a"/>
        <stop offset="1" stop-color="#b25a2c"/>
      </linearGradient>
    </defs>
    <rect width="600" height="777" fill="url(#sceneTone)"/>
  </svg>
  <div class="abs brand"><span class="brand-dot"></span><span class="brand-name">Stone and Brook</span></div>
  <p class="abs tagline">Strenghten the <b>Body.</b><br>Empower the <b>Mind.</b><br>Transform the <b>Soul.</b></p>
  <div class="abs script cover-name">Your Name here</div>
  <p class="abs cover-quote">improve the quality of their relationships.</p>

</main>
</body>
</html>
```